Penny Harvest

Logo and general packaging design for premium quality, price conscious super foods.

Initial product portfolio includes:

Organic Raw Chia Seeds - Resealable plastic bags with 3 x 5 label.
Organic Cold Pressed Coconut Oil (plastic jar) - 2.5 x 6.5 label

The design should be transferable to additional products.

Project requirements:

The design should be simple and the core trade dress should be no more than 2 or 3 colors. The logo should reproduce well in black/1 color.

The idea of this design is to convey quality and simplicity, like a "no frills", premium quality brand.

Deliverable: fully editable (text and illustration):

Logo.

Basic Jar label design.

Basic Bag label design.

Target Market(s)

Educated women aged 22-45

Industry/Entity Type

Plastic

Requirements
Must have
• Clear, simple logo, delivered in vector form, 1 color/black.
• Use of logo on 1 jar label and 1 bag label, each with product name and space for required and optional marketing content.
Nice to have
• Additional iterations of the design to demonstrate your concept of how we will visually vary additional items in jars and bags.
• i.e. What an additional product in a bag would look like for purposes of brand consistency and product differentiation on shelf or online in e-store.
Should not have
• overly detailed graphics that don't scale well and/or may be hard to read or understand. 4 color design elements (except to simiulate how the product may look through the clear jar or bag or how the product may be placed in a simulated surrounding or ad.

```html
<!DOCTYPE html>
<html lang="en">
<head>
<meta charset="utf-8">
<title>Penny Harvest – Logo and Labels</title>
<link rel="stylesheet" href="https://fonts.googleapis.com/css2?family=Oswald:wght@400;500&display=swap">
<style>
  :root {
    --bg: #c8c8c8;
    --paper: #ffffff;
    --band: #a67b50;
    --brand-green: #82c891;
    --detail-brown: #a47a4e;
    --coconut-teal: #4f9ea4;
    --pecan-pink: #d0566a;
    --chia-orange: #f07e2a;
    --rule: #b89a76;
  }
  html, body {
    margin: 0;
    padding: 0;
    width: 1200px;
    height: 1000px;
    overflow: hidden;
    background: var(--bg);
    font-family: "Oswald", "Arial Narrow", sans-serif;
  }
  .canvas {
    position: relative;
    width: 1200px;
    height: 1000px;
  }
  .logo-card {
    position: absolute;
    left: 403px;
    top: 0;
    width: 396px;
    height: 220px;
    background: var(--paper);
    box-shadow: 0 6px 18px rgba(0,0,0,0.18);
    display: flex;
    align-items: center;
    justify-content: center;
    gap: 14px;
  }
  .brand-mark {
    width: 22px;
    height: 22px;
    border-radius: 50%;
    background: var(--brand-green);
  }
  .brand-name {
    font-weight: 500;
    color: var(--brand-green);
    text-transform: uppercase;
    letter-spacing: 1px;
    line-height: 1;
  }
  .logo-card .brand-name { font-size: 56px; }

  .label {
    position: absolute;
    background: var(--paper);
    box-shadow: 0 4px 12px rgba(0,0,0,0.12);
  }
  .label-band {
    background: var(--band);
    display: flex;
    align-items: center;
    justify-content: center;
    gap: 7px;
  }
  .label-band .brand-mark { width: 9px; height: 9px; }
  .label-band .brand-name { font-size: 21px; }
  .label-body { padding: 14px 16px 0; }
  .product-kind {
    font-weight: 400;
    text-transform: uppercase;
    font-size: 24px;
    line-height: 1;
    letter-spacing: 0.5px;
  }
  .product-name {
    font-weight: 500;
    text-transform: uppercase;
    font-size: 44px;
    line-height: 1.05;
    margin-top: 2px;
  }
  .product-info {
    display: flex;
    align-items: flex-start;
    gap: 6px;
    margin-top: 4px;
    color: var(--detail-brown);
  }
  .net-weight { font-weight: 500; font-size: 16px; line-height: 1.2; }
  .net-weight small { font-size: 10px; }
  .info-text {
    border-left: 1px dashed var(--rule);
    padding-left: 6px;
    line-height: 1.15;
  }
  .info-lead { font-size: 11px; font-weight: 500; display: block; }
  .info-fine { font-size: 8px; display: block; }
  .info-rule {
    border-top: 1px dashed var(--rule);
    margin-top: 4px;
  }

  .jar-label { left: 110px; top: 560px; width: 300px; }
  .jar-label .label-band { height: 96px; }
  .jar-label .product-kind { color: var(--coconut-teal); font-size: 23px; }
  .jar-label .product-name { color: var(--coconut-teal); font-size: 46px; }
  .jar-label .label-body { padding-bottom: 16px; }

  .pecan-label { left: 470px; top: 480px; width: 300px; }
  .pecan-label .label-band { height: 88px; }
  .pecan-label .product-kind,
  .pecan-label .product-name { color: var(--pecan-pink); }
  .pecan-label .label-body { padding-bottom: 18px; }

  .chia-label { left: 810px; top: 560px; width: 270px; }
  .chia-label .label-band { height: 62px; }
  .chia-label .product-kind,
  .chia-label .product-name { color: var(--chia-orange); }
  .chia-label .label-body { padding-bottom: 22px; }
</style>
</head>
<body>
<main class="canvas">
  <section class="logo-card" aria-label="Penny Harvest logo">
    <span class="brand-mark"></span>
    <span class="brand-name">Penny Harvest</span>
  </section>

  <article class="label jar-label" aria-label="Coconut oil jar label">
    <header class="label-band">
      <span class="brand-mark"></span>
      <span class="brand-name">Penny Harvest</span>
    </header>
    <div class="label-body">
      <div class="product-kind">Organic Cold Pressed</div>
      <div class="product-name">Coconut Oil</div>
      <div class="product-info">
        <span class="net-weight">500<small>ml</small></span>
        <span class="info-text">
          <span class="info-lead">Cold-pressed, extra virgin, Neutral taste</span>
          <span class="info-fine">Store in a cool dry place after opening</span>
        </span>
      </div>
    </div>
  </article>

  <article class="label pecan-label" aria-label="Pecan nuts bag label">
    <header class="label-band">
      <span class="brand-mark"></span>
      <span class="brand-name">Penny Harvest</span>
    </header>
    <div class="label-body">
      <div class="product-kind">Organic Raw</div>
      <div class="product-name">Pecan Nuts</div>
      <div class="product-info">
        <span class="net-weight">250<small>gr</small></span>
        <span class="info-text">
          <span class="info-lead">Glueten free, Omega 3</span>
          <span class="info-fine">Packed in a facility that handles tree nuts</span>
        </span>
      </div>
      <div class="info-rule"></div>
    </div>
  </article>

  <article class="label chia-label" aria-label="Chia seeds bag label">
    <header class="label-band">
      <span class="brand-mark"></span>
      <span class="brand-name">Penny Harvest</span>
    </header>
    <div class="label-body">
      <div class="product-kind">Organic Raw</div>
      <div class="product-name">Chia Seads</div>
      <div class="product-info">
        <span class="net-weight">250<small>gr</small></span>
        <span class="info-text">
          <span class="info-lead">Glueten free, Omega 3</span>
          <span class="info-fine">Add a spoonful to smoothies, oats or yoghurt</span>
        </span>
      </div>
      <div class="info-rule"></div>
    </div>
  </article>
</main>
</body>
</html>
```